Motivational Poster Design Project

I would like to create a poster with some of my favorite quotes to hang in my office. I did a similar project in 2012 and I've uploaded the top 2 designs so you can get a better idea of what I'm looking for. I will provide feedback on your design within 24 hours of receiving it.

The poster must contain the following quotes:

"You’re only given a little spark of madness. You mustn’t lose it.”
- Dorian Halbrook

“The most contrarian thing of all is not to oppose the crowd but to think for yourself.”
- Marcus Vell

"I constantly see people rise in life who are not the smartest, sometimes not even the most diligent, but they are learning machines. They go to bed every night a little wiser than they were when they got up and boy does that help, particularly when you have a long run ahead of you."
- Walter Brisco

“In theory, there’s no difference between theory and practice. But, in practice, there is.”
- Piet R. K. Ter Wolvenkamp

"At the end of the day, a reactionary life is a normal life. One thing is consistent in every remarkable person: they decide to do something remarkable. Don’t let the world choose who you become."
- Ravindra Kolpe

“It usually takes 3-4 months to try enough that you can do a proper 80/20 analysis, then two months to design systems to scale what *is* working.”
-Gus Ambery

“Authority is 20 percent given, 80 percent taken.”
- Harold Quimsby

“Your actions are consistent with the way the world occurs to you.”
- Anselm Grottke

Project Deadline Extended
Reason: I am going to be travelling with no access to internet until January 5th, 2015. I am extending the project deadline until 12/31/14 and I'll make a final decision during the 1st week of January.

Target Market(s)

Personal Project

Industry/Entity Type

Learning

Requirements
Must have
• The poster will be 24" high x 36" long and printed on canvas, so the image you create needs to have a resolution of at least 2700 x 3900.
Nice to have
• I don't have an exact vision for how the poster should look, so I am totally open to you using your creativity to develop, arrange and present the content as you'd like.
• That said, I would like an image (photo or posterized image) of the person being quoted along with each quote. I do not have specific images that I would like you to use, so you will need to find the images on your own. The images don't need to be perfect... I am more interested in the poster relating the essence of the quotes and the people being quoted than I am in perfect photographic images of the people being quoted.

```html
<!DOCTYPE html>
<html lang="en">
<head>
<meta charset="utf-8">
<title>Quotes Poster</title>
<link href="https://fonts.googleapis.com/css2?family=Titillium+Web:ital,wght@1,300;1,400&display=swap" rel="stylesheet">
<style>
  :root {
    --wood-light: #b9ab93;
    --wood-mid: #a07a4c;
    --wood-warm: #c98a3c;
    --wood-dark: #6e4a26;
    --band-orange: #e2782a;
    --band-blue: #1d3a92;
    --band-red: #c42a2c;
    --band-green: #5b9c1f;
    --band-brown: #8f4c22;
    --band-olive: #a98b18;
    --band-purple: #5c2070;
    --band-dark: #2b2b22;
    --ink: #ffffff;
  }
  html, body {
    margin: 0;
    padding: 0;
    width: 800px;
    height: 1200px;
    overflow: hidden;
  }
  .poster {
    position: relative;
    width: 800px;
    height: 1200px;
    overflow: hidden;
    background:
      radial-gradient(ellipse at 70% 45%, rgba(230,160,70,0.55), transparent 60%),
      linear-gradient(90deg, var(--wood-light) 0%, var(--wood-mid) 35%, var(--wood-warm) 70%, var(--wood-dark) 100%);
    font-family: "Titillium Web", "Myriad Pro", sans-serif;
  }
  .band {
    position: absolute;
    left: 28px;
    width: 744px;
    box-shadow: 0 1px 3px rgba(0,0,0,0.35);
  }
  .band::before {
    content: "";
    position: absolute;
    left: 0; top: 0; bottom: 0;
    width: 150px;
    background: linear-gradient(90deg, rgba(0,0,0,0.35), rgba(0,0,0,0));
  }
  .band--orange { top: 20px;  height: 128px; background: linear-gradient(90deg, var(--band-orange), #e98d3c); }
  .band--blue   { top: 156px; height: 122px; background: linear-gradient(90deg, var(--band-blue), #2846a3); }
  .band--red    { top: 287px; height: 146px; background: linear-gradient(90deg, var(--band-red), #cf3a2e); }
  .band--green  { top: 444px; height: 134px; background: linear-gradient(90deg, #4a8a18, var(--band-green) 55%, #6aa528); }
  .band--brown  { top: 591px; height: 150px; background: linear-gradient(90deg, var(--band-brown), #9a5a2c); }
  .band--olive  { top: 750px; height: 139px; background: linear-gradient(90deg, var(--band-olive), #b69a22 50%, #9e8418); }
  .band--purple { top: 898px; height: 124px; background: linear-gradient(90deg, var(--band-purple), #6a2a80); }
  .band--dark   { top: 1031px; height: 138px; background: linear-gradient(90deg, var(--band-dark), #3a3a2e); }

  .portrait {
    position: absolute;
    left: 58px;
    top: 50%;
    width: 128px;
    height: 128px;
    margin-top: -64px;
    border-radius: 50%;
    box-shadow: 0 2px 6px rgba(0,0,0,0.5);
  }
  .portrait--warm  { background: radial-gradient(circle at 50% 40%, #8a6a58, #2a1c16 80%); }
  .portrait--cool  { background: radial-gradient(circle at 50% 40%, #b4705a, #1a1418 80%); }
  .portrait--pale  { background: radial-gradient(circle at 50% 40%, #d8b8a6, #3a2a24 80%); }
  .portrait--mono  { background: radial-gradient(circle at 50% 40%, #c8c8c0, #1c1c1c 80%); }
  .portrait--light { background: radial-gradient(circle at 50% 40%, #e8c8b0, #f4f0ea 80%); }
  .portrait--glow  { background: radial-gradient(circle at 50% 40%, #d89a7a, #f4ece4 80%); }
  .portrait--red   { background: radial-gradient(circle at 50% 40%, #c48070, #2a1a1a 80%); }

  .quote {
    position: absolute;
    left: 200px;
    right: 20px;
    top: 50%;
    transform: translateY(-50%);
    margin: 0;
    color: var(--ink);
    text-align: center;
    font-style: italic;
    font-weight: 300;
    font-size: 19.5px;
    line-height: 1.22;
    text-shadow: 0 1px 2px rgba(0,0,0,0.3);
  }
  .quote__author { display: block; }
</style>
</head>
<body>
<main class="poster">
  <section class="band band--orange">
    <div class="portrait portrait--warm" role="img" aria-label="Portrait of Dorian Halbrook"></div>
    <p class="quote">"You're only given a little spark of madness. You mustn't lose it."<span class="quote__author">- Dorian Halbrook</span></p>
  </section>
  <section class="band band--blue">
    <div class="portrait portrait--cool" role="img" aria-label="Portrait of Marcus Vell"></div>
    <p class="quote">"The most contrarian thing of all is not to oppose the crowd<br>but to think for yourself."<span class="quote__author">- Marcus Vell</span></p>
  </section>
  <section class="band band--red">
    <div class="portrait portrait--pale" role="img" aria-label="Portrait of Walter Brisco"></div>
    <p class="quote">"I constantly see people rise in life who are not the smartest,<br>sometimes not even the most diligent, but they are learning machines.<br>They go to bed every night a little wiser than they were when they<br>got up and boy does that help, particularly when you have a long<br>run ahead of you." - Walter Brisco</p>
  </section>
  <section class="band band--green">
    <div class="portrait portrait--mono" role="img" aria-label="Portrait of Piet R. K. Ter Wolvenkamp"></div>
    <p class="quote">"In theory, there's no difference between theory and practice.<br>But, in practice, there is."<span class="quote__author">- Piet R. K. Ter Wolvenkamp</span></p>
  </section>
  <section class="band band--brown">
    <div class="portrait portrait--light" role="img" aria-label="Portrait of Ravindra Kolpe"></div>
    <p class="quote">"At the end of the day, a reactionary life is a normal life.<br>One thing is consistent in every remarkable person:<br>they decide to do something remarkable.<br>Don't let the world choose who you become."<span class="quote__author">- Ravindra Kolpe</span></p>
  </section>
  <section class="band band--olive">
    <div class="portrait portrait--glow" role="img" aria-label="Portrait of Gus Ambery"></div>
    <p class="quote">"It usually takes 3-4 months to try enough that you can do a<br>proper 80/20 analysis, then two months to design<br>systems to scale what *is* working."<span class="quote__author">-Gus Ambery</span></p>
  </section>
  <section class="band band--purple">
    <div class="portrait portrait--red" role="img" aria-label="Portrait of Harold Quimsby"></div>
    <p class="quote">"Authority is 20 percent given, 80 percent taken."<span class="quote__author">- Harold Quimsby</span></p>
  </section>
  <section class="band band--dark">
    <div class="portrait portrait--red" role="img" aria-label="Portrait of Anselm Grottke"></div>
    <p class="quote">"Your actions are consistent with the way the world occurs to you."<span class="quote__author">- Anselm Grottke</span></p>
  </section>
</main>
</body>
</html>
```